Webdesign für Restaurant / Lale Grillstube
Zielgruppe
Wir führen ein türkisches Restaurant/Imbiss mit einem Catering Service und Lieferservice. Unser Betrieb ist ein 'zwischen Ding'.
Sie können es sich wie ein türkisches 'Morgenhof' oder 'Bistro Vila' vorstellen.
Wir haben Sitzplätze und Laufkundschaft.
Zielgruppe:
Jeder der gerne gutes Essen isst.
Aufgabenstellung
Unsere Webseite soll ein "Onepager" werden.
Sie sollte auch für mobil Geräte optimiert sein.
Die Internetseite soll bei dem Interessenten folgenden Eindruck hinterlassen: Dass wir wissen was wir machen, dass wir professionell arbeiten und dass sie bei uns qualitativ hochwertiges Essen bekommen.
Die folgende Seite gefällt mir sehr gut:
http://www.quill-bistro.example
Die Funktionsweise (Auf die Menüpunkte drücken und runterscrollen) soll die gleiche, wie auf dieser Seite sein.
Was mich an dieser Seite stört:
Die Startseite(ganz oben) wirkt meiner Meinung nach etwas "lasch". Sie wirkt etwas zu grau, leblos. Zu dunkel gehalten.
Sie sollten sich trotzdem an der erwähnten Seite orientieren, da mir der Aufbau und die sonstige Gestaltung sehr gut gefällt.
Sie können sich auch an dieser Seite orientieren:
https://www.zahlwerk.example
Farben: keine konkrete Vorstellung. Sollte sich jedoch nicht mit unserem Logo beißen.
Bilder: Sie haben freie Wahl. Wenn Sie Bilder von Speisen verwenden, sollten Sie sich an
unserer Speisekarte orientieren.
Ich sende ihnen Bilder zu, die Sie nutzen können. Müssen Sie aber nicht.
Bilder sind gekauft oder selbst gemacht.
Aufbau und Elemente zu den jeweiligen Abschnitten:
- Home: Catering sollte etwas hervorgehoben werden
Unsere Telefonnummer sollte leicht zu finden sein.
Beispiel: https://www.tarnfeld.example/de/
Hintergrundbild: Ansprechendes Foto von einem Gericht(Essen)
- Anschrift
- Öffnungszeiten
- Link zu unserer Netzwerkseite
- (Impressum hier enthalten)
- Catering
- Lieferservice
- Menu: Unsere Speisen sollten hier übersichtlich auftauchen. (Unsere Karte finden sie auf
- Getränke: Unsere Getränke sollten hier übersichtlich auftauchen
Texte zu den Menüpunkten: <..

```html
<!DOCTYPE html>
<html lang="de">
<head>
<meta charset="utf-8">
<title>Lale Grillstube – Restaurant, Catering &amp; Lieferservice</title>
<link href="https://fonts.googleapis.com/css2?family=Montserrat:wght@300;400;600;700&family=Open+Sans:ital,wght@0,400;0,600;0,700;1,400&display=swap" rel="stylesheet">
<style>
:root{
  --green:#1f8a3e;
  --green-dark:#17692f;
  --ink:#333333;
  --muted:#8a8a8a;
  --line:#e3e3e3;
  --bar:#3b3b3b;
  --footer:#3a3a3a;
  --footer-bottom:#2b2b2b;
  --white:#ffffff;
}
*{margin:0;padding:0;box-sizing:border-box}
html,body{width:1200px;height:5352px;overflow:hidden}
body{font-family:"Open Sans",Arial,sans-serif;color:var(--ink);background:var(--white);position:relative}
.wrap{width:731px;margin:0 auto;position:relative}

/* navigation */
.nav{position:absolute;left:0;width:1200px;display:flex;align-items:center;font-family:"Montserrat",Arial,sans-serif;font-weight:600;font-size:11px;color:var(--white)}
.nav span{position:absolute;white-space:nowrap}
.nav .brand{display:flex;align-items:center;gap:8px;transform:translateX(-50%);font-size:16px;font-weight:700}
.nav .brand i{width:14px;height:14px;border-radius:50%;background:var(--green);display:block}
.nav .dot{width:16px;height:16px;border-radius:50%;background:var(--white);display:block}

/* hero */
.hero{position:absolute;top:0;left:0;width:1200px;height:607px;background:radial-gradient(ellipse at 50% 45%,#6b5a44 0%,#3e352c 45%,#1e1b18 100%)}
.hero-nav{top:87px}
.hero h1{position:absolute;top:288px;width:100%;text-align:center;font-family:"Montserrat",Arial,sans-serif;font-weight:600;font-size:30px;color:var(--white);letter-spacing:.5px}
.hero .sub{position:absolute;top:344px;width:100%;text-align:center;font-family:"Montserrat",Arial,sans-serif;font-weight:300;font-size:23px;color:var(--white)}

.stickybar{position:absolute;top:607px;left:0;width:1200px;height:58px;background:var(--bar)}
.stickybar .nav{top:29px}
.stickybar .brand{font-size:12px}

/* about */
.about{position:absolute;top:665px;left:0;width:1200px;height:411px}
.about .left{position:absolute;left:235px;top:57px;width:480px}
.section-title{font-family:"Montserrat",Arial,sans-serif;font-weight:600;font-size:28px;color:var(--green);letter-spacing:.3px}
.section-sub{font-size:17px;color:var(--ink);margin-top:4px}
.small{font-size:9.5px;line-height:22px;color:var(--muted)}
.about .small{margin-top:32px}
.about .small+.small{margin-top:10px}
.about .right{position:absolute;left:798px;top:58px;width:170px;font-size:9.5px;line-height:18px;color:var(--muted)}
.about .right b{display:block;color:var(--ink);font-weight:600;font-size:9px;text-transform:uppercase}
.about .right p{margin-bottom:20px}

.photo{position:absolute;left:0;width:1200px}
.photo-pizza{top:1076px;height:376px;background:linear-gradient(100deg,#5a2e1a 0%,#a3472a 35%,#7a4a2c 60%,#3a2418 100%)}

/* menu */
.menu-block{position:absolute;left:235px;width:731px}
.menu-head{text-align:center}
.menu-head svg{display:block;margin:0 auto}
.menu-head h2{font-family:"Montserrat",Arial,sans-serif;font-weight:600;font-size:17px;color:var(--green);margin-top:10px;letter-spacing:.5px}
.items{display:grid;grid-template-columns:313px 323px;column-gap:95px;margin-top:26px}
.item{height:57.5px;position:relative}
.item .name{font-size:11px;color:var(--ink)}
.item .price{position:absolute;right:0;top:1px;font-size:10px;color:var(--muted)}
.item .desc{font-size:8.5px;font-style:italic;color:var(--muted);padding-left:33px;line-height:12px;width:260px}
.divider{position:absolute;left:235px;width:731px;height:1px;background:var(--line)}

/* testimonial */
.testimonial{position:absolute;top:3102px;left:0;width:1200px;height:374px;background:linear-gradient(90deg,#2c3a22 0%,#4a3522 40%,#3d2a1c 70%,#2a2018 100%)}
.testimonial h3{position:absolute;top:122px;width:100%;text-align:center;font-size:15px;font-weight:600;color:var(--white)}
.testimonial blockquote{position:absolute;top:162px;left:300px;width:600px;text-align:center;font-style:italic;font-size:13px;line-height:23px;color:var(--white)}
.dots{position:absolute;top:296px;width:100%;display:flex;justify-content:center;gap:10px}
.dots i{width:6px;height:6px;border-radius:50%;background:rgba(255,255,255,.6);display:block}
.dots i:first-child{background:var(--white)}

/* catering & delivery */
.feature{position:absolute;left:0;width:1200px}
.feature .text{position:absolute;width:358px}
.feature .section-sub{margin-top:8px}
.feature .small{margin-top:26px}
.feature .small+.small{margin-top:12px}
.feature .img{position:absolute}
.catering{top:3532px;height:260px}
.catering .text{left:235px;top:0}
.catering .img{left:608px;top:5px;width:358px;height:249px;background:linear-gradient(135deg,#c9c2b6 0%,#8a5a42 45%,#b8482c 70%,#e8e2d8 100%)}
.delivery{top:3918px;height:260px}
.delivery .img{left:235px;top:5px;width:355px;height:253px;background:linear-gradient(135deg,#2b1e16 0%,#6a3220 40%,#9a5a2a 65%,#2a1f18 100%)}
.delivery .text{left:608px;top:0}

/* appetite band */
.appetite{position:absolute;top:4239px;left:0;width:1200px;height:343px;background:linear-gradient(90deg,#4a3020 0%,#7a4a2a 40%,#5a3826 70%,#3a2a20 100%)}
.appetite h2{position:absolute;top:40px;width:100%;text-align:center;font-family:"Montserrat",Arial,sans-serif;font-weight:600;font-size:28px;color:var(--white)}
.appetite p{position:absolute;left:315px;width:570px;text-align:center;font-size:12.5px;line-height:19px;color:var(--white)}
.appetite .p1{top:110px}
.appetite .p2{top:215px}

.map{position:absolute;top:4582px;left:0;width:1200px;height:342px;background:linear-gradient(180deg,#f1f1f1,#e6e6e6)}
.map svg{position:absolute;left:710px;top:113px}

/* footer */
.footer{position:absolute;top:4924px;left:0;width:1200px;height:387px;background:var(--footer);color:var(--white);text-align:center}
.footer .brand{position:absolute;top:92px;width:100%;display:flex;justify-content:center;align-items:center;gap:10px;font-family:"Montserrat",Arial,sans-serif;font-weight:700;font-size:22px}
.footer .brand i{width:18px;height:18px;border-radius:50%;background:var(--green);display:block}
.footer address{position:absolute;top:202px;width:100%;font-style:normal;font-size:10px;line-height:15px}
.footer address .gap{margin-top:15px}
.footer .social{position:absolute;top:329px;left:588px;width:24px;height:24px;border-radius:50%;background:var(--white)}
.copy{position:absolute;top:5311px;left:0;width:1200px;height:41px;background:var(--footer-bottom);color:var(--white);font-size:9px;text-align:center;line-height:41px;letter-spacing:.3px}
</style>
</head>
<body>

<header class="hero" role="img" aria-label="Foto: gefüllte Teigrollen mit Kräutern in einer Pfanne">
  <nav class="nav hero-nav">
    <span style="left:235px">Menü</span>
    <span style="left:328px">Lieferservice</span>
    <span style="left:459px">Catering</span>
    <span class="brand" style="left:600px"><i></i>Lale Grillstube</span>
    <span style="left:696px">Über uns</span>
    <span style="left:758px">Kontakt</span>
    <span style="left:814px">|</span>
    <span style="left:831px">+49-2302-48150</span>
    <span style="left:928px">|</span>
    <span class="dot" style="left:948px;top:-8px"></span>
  </nav>
  <h1>GESCHMACK UND QUALITÄT IN TRADITION</h1>
  <div class="sub">ÜBER 20 JAHRE</div>
</header>

<div class="stickybar">
  <nav class="nav">
    <span style="left:235px">Menü</span>
    <span style="left:328px">Lieferservice</span>
    <span style="left:459px">Catering</span>
    <span class="brand" style="left:600px"><i></i>Lale Grillstube</span>
    <span style="left:696px">Über uns</span>
    <span style="left:758px">Kontakt</span>
    <span style="left:814px">|</span>
    <span style="left:831px">+49-2302-48150</span>
    <span style="left:928px">|</span>
    <span class="dot" style="left:948px;top:-8px"></span>
  </nav>
</div>

<section class="about">
  <div class="left">
    <h2 class="section-title">LALE GRILLSTUBE</h2>
    <p class="section-sub">Ein Familienbetrieb in zweiter Generation</p>
    <p class="small">Die Lale Grillstube ist ein Familienbetrieb in zweiter Generation und seit 1992 in Talbruch tätig. In über 20 Jahren haben wir viele Stammkunden gewinnen können. Aus den Mitteilungen und Forenbeiträgen unserer Kunden erfahren wir, dass so manche gerne einen weiteren Weg kommen (ca. 60 km - nach unseren Erfahrungen), um unsere Köstlichkeiten zu verspeisen. "Wann machen Sie endlich eine Filiale in unserer Nähe auf?" werden wir gefragt, was uns natürlich sehr schmeichelt.</p>
    <p class="small">Dieses Feedback gab uns unter Anderem den Anstoß, das alte Kebaphaus neu zu errichten. Seit Anfang 2016 sind wir in dem Neubau, unter der Hausnummer 27 zu finden. Dort finden unsere Gäste ein größeres und moderneres Haus für sich und ihre Lieben.</p>
  </div>
  <div class="right">
    <p><b>Telefon:</b>+49 230248150</p>
    <p><b>Lieferservice und Catering:</b>02302 48150<br>01577 3926514</p>
    <p><b>E-Mail:</b>info@lalegrillstube.de</p>
    <p><b>Standort:</b>Lindenweg 27<br>58100 Talbruch</p>
    <p><b>Öffnungszeiten:</b>Mo-So: von 7.00 bis 23.00</p>
  </div>
</section>

<div class="photo photo-pizza" role="img" aria-label="Foto: türkische Pide mit Hackfleisch und roten Chilischoten auf Holz"></div>

<!-- Pizzen -->
<section class="menu-block" style="top:1515px">
  <div class="menu-head">
    <svg width="64" height="66" viewBox="0 0 64 66" fill="none" stroke="#555" stroke-width="2">
      <circle cx="32" cy="38" r="24"/><circle cx="32" cy="38" r="18"/>
      <path d="M14 22 L32 38 L50 10"/><circle cx="26" cy="44" r="3"/><circle cx="38" cy="46" r="2.5"/><circle cx="30" cy="28" r="2"/>
    </svg>
    <h2>PIZZEN</h2>
  </div>
  <div class="items">
    <div class="item"><div class="name">110. Pizza Bella Margherita</div><div class="price">4.80 €</div><div class="desc">Tomatensoße, Gouda</div></div>
    <div class="item"><div class="name">116. Pizza Bella Margherita</div><div class="price">4.80 €</div><div class="desc">Tomatensoße, Gouda</div></div>
    <div class="item"><div class="name">111. Pizza Pomodoro</div><div class="price">5.80 €</div><div class="desc">Tomatensoße, Gouda, Tomaten</div></div>
    <div class="item"><div class="name">117. Pizza Pomodoro</div><div class="price">5.80 €</div><div class="desc">Tomatensoße, Gouda, Sucuk (türk Knoblauchwurst), Jalapenos, scharfes Paprikapulver</div></div>
    <div class="item"><div class="name">112. Pizza Mediterrano</div><div class="price">6.50 €</div><div class="desc">Tomatensoße, Gouda, Brokkoli, Paprika, Oliven</div></div>
    <div class="item"><div class="name">118. Pizza Mediterrano</div><div class="price">6.50 €</div><div class="desc">Tomatensoße, Gouda, Brokkoli, Paprika, Oliven</div></div>
    <div class="item"><div class="name">113. Pizza Pomodoro</div><div class="price">6.90 €</div><div class="desc">Tomatensoße, Gouda, Tomaten</div></div>
    <div class="item"><div class="name">119. Pizza Pomodoro</div><div class="price">6.90 €</div><div class="desc">Tomatensoße, Gouda, Tomaten</div></div>
    <div class="item"><div class="name">114. Pizza Piccante</div><div class="price">6.50 €</div><div class="desc">Tomatensoße, Gouda, Sucuk (türk Knoblauchwurst), Jalapenos, scharfes Paprikapulver</div></div>
    <div class="item"><div class="name">120. Pizza Piccante</div><div class="price">6.50 €</div><div class="desc">Tomatensoße, Gouda, Sucuk (türk Knoblauchwurst), Jalapenos, scharfes Paprikapulver</div></div>
    <div class="item"><div class="name">115. Pizza Pomodoro</div><div class="price">6.90 €</div><div class="desc">Tomatensoße, Gouda, Tomaten</div></div>
    <div class="item"><div class="name">121. Pizza Pomodoro</div><div class="price">6.90 €</div><div class="desc">Tomatensoße, Gouda, Tomaten</div></div>
  </div>
</section>
<div class="divider" style="top:2015px"></div>

<!-- Hauptgerichte -->
<section class="menu-block" style="top:2055px">
  <div class="menu-head">
    <svg width="64" height="66" viewBox="0 0 64 66" fill="none" stroke="#555" stroke-width="2">
      <circle cx="32" cy="12" r="3"/><path d="M8 52 A24 24 0 0 1 56 52 Z"/><path d="M2 58 H62"/><path d="M32 15 V28"/>
    </svg>
    <h2>HAUPTGERICHTE</h2>
  </div>
  <div class="items">
    <div class="item"><div class="name">110. Pizza Bella Margherita</div><div class="price">4.80 €</div><div class="desc">Tomatensoße, Gouda</div></div>
    <div class="item"><div class="name">116. Pizza Bella Margherita</div><div class="price">4.80 €</div><div class="desc">Tomatensoße, Gouda</div></div>
    <div class="item"><div class="name">111. Pizza Pomodoro</div><div class="price">5.80 €</div><div class="desc">Tomatensoße, Gouda, Tomaten</div></div>
    <div class="item"><div class="name">117. Pizza Pomodoro</div><div class="price">5.80 €</div><div class="desc">Tomatensoße, Gouda, Sucuk (türk Knoblauchwurst), Jalapenos, scharfes Paprikapulver</div></div>
    <div class="item"><div class="name">112. Pizza Mediterrano</div><div class="price">6.50 €</div><div class="desc">Tomatensoße, Gouda, Brokkoli, Paprika, Oliven</div></div>
    <div class="item"><div class="name">118. Pizza Mediterrano</div><div class="price">6.50 €</div><div class="desc">Tomatensoße, Gouda, Brokkoli, Paprika, Oliven</div></div>
    <div class="item"><div class="name">113. Pizza Pomodoro</div><div class="price">6.90 €</div><div class="desc">Tomatensoße, Gouda, Tomaten</div></div>
    <div class="item"><div class="name">119. Pizza Pomodoro</div><div class="price">6.90 €</div><div class="desc">Tomatensoße, Gouda, Tomaten</div></div>
    <div class="item"><div class="name">114. Pizza Piccante</div><div class="price">6.50 €</div><div class="desc">Tomatensoße, Gouda, Sucuk (türk Knoblauchwurst), Jalapenos, scharfes Paprikapulver</div></div>
    <div class="item"><div class="name">120. Pizza Piccante</div><div class="price">6.50 €</div><div class="desc">Tomatensoße, Gouda, Sucuk (türk Knoblauchwurst), Jalapenos, scharfes Paprikapulver</div></div>
    <div class="item"><div class="name">115. Pizza Pomodoro</div><div class="price">6.90 €</div><div class="desc">Tomatensoße, Gouda, Tomaten</div></div>
    <div class="item"><div class="name">121. Pizza Pomodoro</div><div class="price">6.90 €</div><div class="desc">Tomatensoße, Gouda, Tomaten</div></div>
  </div>
</section>
<div class="divider" style="top:2560px"></div>

<!-- Getränke -->
<section class="menu-block" style="top:2596px">
  <div class="menu-head">
    <svg width="64" height="66" viewBox="0 0 64 66" fill="none" stroke="#555" stroke-width="2">
      <path d="M10 10 H54 L32 36 Z"/><path d="M32 36 V60"/><path d="M20 61 H44"/><path d="M40 4 L46 22"/><circle cx="24" cy="16" r="3"/>
    </svg>
    <h2>GETRÄNKE</h2>
  </div>
  <div class="items">
    <div class="item"><div class="name">110. Pizza Bella Margherita</div><div class="price">4.80 €</div><div class="desc">Tomatensoße, Gouda</div></div>
    <div class="item"><div class="name">116. Pizza Bella Margherita</div><div class="price">4.80 €</div><div class="desc">Tomatensoße, Gouda</div></div>
    <div class="item"><div class="name">111. Pizza Pomodoro</div><div class="price">5.80 €</div><div class="desc">Tomatensoße, Gouda, Tomaten</div></div>
    <div class="item"><div class="name">117. Pizza Pomodoro</div><div class="price">5.80 €</div><div class="desc">Tomatensoße, Gouda, Sucuk (türk Knoblauchwurst), Jalapenos, scharfes Paprikapulver</div></div>
    <div class="item"><div class="name">112. Pizza Mediterrano</div><div class="price">6.50 €</div><div class="desc">Tomatensoße, Gouda, Brokkoli, Paprika, Oliven</div></div>
    <div class="item"><div class="name">118. Pizza Mediterrano</div><div class="price">6.50 €</div><div class="desc">Tomatensoße, Gouda, Brokkoli, Paprika, Oliven</div></div>
    <div class="item"><div class="name">113. Pizza Pomodoro</div><div class="price">6.90 €</div><div class="desc">Tomatensoße, Gouda, Tomaten</div></div>
    <div class="item"><div class="name">119. Pizza Pomodoro</div><div class="price">6.90 €</div><div class="desc">Tomatensoße, Gouda, Tomaten</div></div>
    <div class="item"><div class="name">114. Pizza Piccante</div><div class="price">6.50 €</div><div class="desc">Tomatensoße, Gouda, Sucuk (türk Knoblauchwurst), Jalapenos, scharfes Paprikapulver</div></div>
    <div class="item"><div class="name">120. Pizza Piccante</div><div class="price">6.50 €</div><div class="desc">Tomatensoße, Gouda, Sucuk (türk Knoblauchwurst), Jalapenos, scharfes Paprikapulver</div></div>
    <div class="item"><div class="name">115. Pizza Pomodoro</div><div class="price">6.90 €</div><div class="desc">Tomatensoße, Gouda, Tomaten</div></div>
    <div class="item"><div class="name">121. Pizza Pomodoro</div><div class="price">6.90 €</div><div class="desc">Tomatensoße, Gouda, Tomaten</div></div>
  </div>
</section>

<section class="testimonial" role="img" aria-label="Foto: Grillfleisch, Zwiebeln und Salat auf Holztisch">
  <h3>John Doe</h3>
  <blockquote>"Lorem ipsum dolor sit amet, consectetur adipiscing elit. Fusce vel libero dui. Nam ac lectus sed ex pulvinar semper. Mauris ac nulla aliquam arcu volutpat maximus. Donec tincidunt sem in nibh venenatis, eleifend fringilla purus vehicula. Morbi consequat ullamcorper odio, id convallis ante dictum at. "</blockquote>
  <div class="dots"><i></i><i></i><i></i><i></i></div>
</section>

<section class="feature catering">
  <div class="text">
    <h2 class="section-title">LALE CATERING</h2>
    <p class="section-sub">Sie benötigen Hilfe bei der Planung?</p>
    <p class="small">Ob Firmenfeste, Geburtstage oder sonstige Events - Lale Grillstube stellt Ihnen ein individuelles Catering Angebot zusammen.</p>
    <p class="small">Ihre Wünsche als Kunde stehen dabei immer im Vordergrund. Buchen Sie Ihr Catering vor Ort oder rufen Sie uns an!</p>
    <p class="small">Unser Team hilft Ihnen gerne weiter.</p>
  </div>
  <div class="img" role="img" aria-label="Foto: Familie an einem festlich gedeckten Tisch mit Essen"></div>
</section>

<section class="feature delivery">
  <div class="img" role="img" aria-label="Foto: gegrillte Steaks mit Gemüse auf dunklem Grund"></div>
  <div class="text">
    <h2 class="section-title">LIEFERSERVICE</h2>
    <p class="section-sub">Sie benötigen Hilfe bei der Planung?</p>
    <p class="small">Wir liefern alle Köstlichkeiten auch ausser Haus. Ein Anruf genügt. Aus dem umfangreichen Speisenangebot können Sie sich Ihre Gerichte zusammenstellen und telefonisch bestellen. Sie haben die Möglichkeit sich von vorne bis hinten bedienen zu lassen. Wir bereiten alles was Sie sich wünschen frisch zu und bringen es entweder an Ihren Tisch oder Sie nehmen es einfach mit nach Hause.</p>
  </div>
</section>

<section class="appetite" role="img" aria-label="Foto: Pizza im Hintergrund">
  <h2>GUTEN APPETIT!</h2>
  <p class="p1">Ausgewogen und Gesund essen. Seit 1992 bieten wir unseren Gästen Frische und Geschmack in höchster Qualität. Das Geheimnis ist sehr einfach:<br>WIR SIND GERNE FÜR SIE DA!<br>IHR LALE GRILLSTUBE TEAM</p>
  <p class="p2">Getränke: Wir bieten natürlich auch eine große Auswahl an Softdrinks, Kaffeespezialitäten sowie Alkoholischen Getränken an. Unsere Empfehlung an Sie: Probieren Sie unseren Ayran bei Ihrem nächsten Besuch.</p>
</section>

<section class="map" role="img" aria-label="Stadtplan mit Standort der Lale Grillstube">
  <svg width="24" height="32" viewBox="0 0 24 32"><path d="M12 0 C5 0 0 5 0 12 C0 21 12 32 12 32 C12 32 24 21 24 12 C24 5 19 0 12 0 Z" fill="#1f8a3e"/><circle cx="12" cy="12" r="4.5" fill="#fff"/></svg>
</section>

<footer class="footer">
  <div class="brand"><i></i>Lale Grillstube</div>
  <address>
    Lale Grillstube<br>
    Inhaber Emre Tandoğan<br>
    Lindenweg 27<br>
    58100 Talbruch
    <div class="gap">Telefon: +49 2302 48150<br>Email: info@lalegrillstube.de</div>
  </address>
  <span class="social"></span>
</footer>
<div class="copy">© 2016 LALEGRILLSTUBE</div>

</body>
</html>
```